Event for Hair Salon Wigs

We are introducing a new division of our hair salon selling hair wigs. We are introducing our clients to our wig line, which are beautiful well crafted wig. These wigs are not like granny's wigs, but wigs for women who want style and are willing to pay extra for beautiful believeable wigs. The event is casual were clients and there friends will be flowing in and out during a sunday afternoon.
The postcard should reflect a nice sunny spring day, but classy not extremely colorful. If you think a photo would add to a better look to the card....let me know and I will upload some.
Thank you

I have images that was uploaded, but have not been posted to this project. I'm not sure what's going on, but please look out for them. I have been trying to communicate with customer service, but no  response thus far. The cards I have received this far I think have to much of a colored pattern, I would love it if the logo "M Lovely Wigs" took center stage, rather than the word open house. Open House is important, but I don't won't it to be bolder than "wigs." Please leave room for address labels, and if possible, the description of the event should be in little bigger text. Oh, I am open to an abstract lady rather than the images that are uploaded, but if images are used, you don't have to use them all. Believe it or not...I do like simplicity:)

```html
<!DOCTYPE html>
<html lang="en">
<head>
<meta charset="utf-8">
<title>M Lovely Wigs – Open House Postcard</title>
<link rel="stylesheet" href="https://fonts.googleapis.com/css2?family=Open+Sans:wght@400;600&display=swap">
<style>
  :root {
    --backdrop: #5b3b26;
    --front-orange: #f07a1c;
    --hair-purple: #6a2a78;
    --cream: #f6e9bd;
    --accent-orange: #f07d2a;
    --body-brown: #6e2f12;
    --white: #ffffff;
  }
  * { margin: 0; padding: 0; box-sizing: border-box; }
  html, body { width: 1200px; height: 675px; overflow: hidden; }
  body {
    background: var(--backdrop);
    font-family: "Open Sans", sans-serif;
    position: relative;
  }
  .postcard {
    position: absolute;
    top: 125px;
    width: 532px;
    height: 414px;
    box-shadow: 0 4px 10px rgba(0,0,0,0.35);
  }
  .postcard-front {
    left: 51px;
    background: var(--front-orange);
    overflow: hidden;
  }
  .hair-figure {
    position: absolute;
    left: 112px;
    top: 0;
    width: 250px;
    height: 414px;
    background: linear-gradient(180deg, #74307f 0%, var(--hair-purple) 100%);
    border-radius: 120px 120px 30px 30px;
  }
  .brand-name {
    position: absolute;
    left: 150px;
    top: 180px;
    width: 250px;
    color: var(--white);
    font-weight: 400;
    font-size: 30px;
    line-height: 1.1;
    text-align: center;
  }
  .front-url {
    position: absolute;
    left: 180px;
    top: 356px;
    width: 160px;
    color: var(--white);
    font-size: 13px;
    text-align: center;
  }
  .postcard-back {
    left: 623px;
    background: var(--cream);
    padding: 8px 10px;
    color: var(--body-brown);
  }
  .event-details { width: 270px; }
  .heading {
    color: var(--accent-orange);
    font-weight: 400;
    font-size: 26px;
    line-height: 1.05;
  }
  .event-when, .invite-text, .signature, .venue {
    font-size: 11.4px;
    line-height: 1.2;
  }
  .event-when { margin-bottom: 4px; }
  .invite-text { margin-top: 1px; }
  .extras {
    font-size: 13.5px;
    font-weight: 600;
    margin: 6px 0;
  }
</style>
</head>
<body>
  <section class="postcard postcard-front">
    <div class="hair-figure" role="img" aria-label="Abstract illustration of a woman's long wavy hair in purple with dots"></div>
    <div class="brand-name">M Lovely Wigs</div>
    <div class="front-url">www.mlovelywigs.com</div>
  </section>

  <section class="postcard postcard-back">
    <div class="event-details">
      <h1 class="heading">Open House</h1>
      <p class="event-when">Sunday April 13th 2014<br>11am to 3pm</p>
      <h2 class="heading">Hello!</h2>
      <p class="invite-text">I would like to cordially invite you to <em>Salon M</em> to introduce you to <em>M Lovely Wigs</em>. A showroom of some of the finest human and synthetic hair wigs available. Come look, feel and try-on these beautiful wigs. <em>M Lovely Wigs</em> can be purchased and ordered the day of the event for an introductory offer of 10% off of the total sales. If you bring a friend or donate a gently warn wig for charity, you will receive 15% off of the total purchase. Additionally, bring a friend and a gently warn wig and receive 20% off of the total purchase. Come join us…you might find a fabulous new look for spring!</p>
      <h2 class="heading">Hope to see you,</h2>
      <p class="signature">Renata Holloway</p>
      <p class="extras">Light appetizers and Drinks, Raffles</p>
      <p class="venue">Salon M<br>4410 Linden Grove Way Ste. B<br>Fairview, Ca 90210<br>(555) 014-2298<br>www.mlovelywigs.com</p>
    </div>
  </section>
</body>
</html>
```